New Business Card for Casual Beachfront Cafe

Quirky Beachfront Cafe at Moana, South Australia needs a DOUBLE SIDED business card to print on PrintHarbor.

Target Market(s)

Business Cards sit on the counter for Guests to take with them. Please view our website www.saltreefcafe.com.au to get a feel for the Cafe. You may also view our Instagram at @saltreefcafe

Industry/Entity Type

Cafe / Restaurant

Contact Information for Business Card

Information equivalent to: Breakfast, Lunch, Dinner, Coffee, Takeaway / 117 Parade Moana SA 5169 / Menu & Opening Hours: www.saltreefcafe.com.au / ph (08) 8461 9273

Requirements
Must have
• Information equivalent to: Breakfast, Lunch, Dinner, Coffee, Takeaway / 117 Parade Moana SA 5169 / Menu & Opening Hours: www.saltreefcafe.com.au / ph (08) 8461 9273
Nice to have
• Potentially some of our trademark colours (Cafe can be searched via Seekly)
Should not have
• Must NOT have image of the building. May have the logo provided on one side but not necessarily, depending on how you wish to design the card

```html
<!DOCTYPE html>
<html lang="en">
<head>
<meta charset="utf-8">
<title>Salt Reef Cafe — Business Card</title>
<link rel="stylesheet" href="https://fonts.googleapis.com/css2?family=Bitter:wght@400;700;800&display=swap">
<style>
  :root {
    --bg: #e9eaea;
    --card: #f7f7f5;
    --ink-blue: #2b5797;
    --sun-yellow: #f2f52e;
  }
  * { margin: 0; padding: 0; box-sizing: border-box; }
  html, body {
    width: 1200px; height: 853px; overflow: hidden;
    background: var(--bg);
    font-family: "Bitter", Georgia, serif;
  }
  .sheet {
    width: 1200px; height: 853px;
    display: flex; align-items: center; justify-content: center; gap: 60px;
  }
  .card {
    position: relative;
    width: 500px; height: 286px;
    background: var(--card);
    border-radius: 24px;
    overflow: hidden;
    box-shadow: 0 6px 18px rgba(0,0,0,0.12);
  }
  .front-artwork {
    position: absolute; inset: 0;
    background: linear-gradient(100deg, var(--card) 0%, #f5f6b8 35%, var(--sun-yellow) 70%);
  }
  .brand-name {
    position: absolute;
    right: 40px; top: 50%;
    transform: translateY(-50%);
    color: var(--ink-blue);
    font-weight: 800;
    font-size: 34px;
    line-height: 1.1;
    text-transform: uppercase;
    text-align: center;
  }
  .card-back {
    display: flex; flex-direction: column; align-items: center;
    padding-top: 34px;
    color: var(--ink-blue);
    text-align: center;
  }
  .back-rule { width: 380px; height: 2px; background: var(--ink-blue); margin-bottom: 12px; }
  .back-title { font-weight: 700; font-size: 27px; letter-spacing: 0.5px; margin-bottom: 12px; }
  .back-line { font-size: 15px; line-height: 1.45; }
  .back-strong { font-weight: 700; font-size: 17px; margin-top: 10px; }
  .back-phone { font-weight: 700; font-size: 16px; margin-top: 14px; }
</style>
</head>
<body>
  <main class="sheet">
    <section class="card card-front" aria-label="Card front">
      <div class="front-artwork" role="img" aria-label="Decorative yellow and white wave pattern with stitched edges"></div>
      <div class="brand-name">Salt Reef<br>Cafe</div>
    </section>

    <section class="card card-back" aria-label="Card back">
      <div class="back-rule"></div>
      <h1 class="back-title">SALT REEF CAFE</h1>
      <p class="back-line">Breakfast, Lunch, Dinner, Coffee, Takeaway</p>
      <p class="back-line">117 Parade Moana SA 5169</p>
      <p class="back-line back-strong">For Menu &amp; Opening hours</p>
      <p class="back-line">check the website</p>
      <p class="back-line">www.saltreefcafe.com.au</p>
      <p class="back-line back-phone">ph (08) 8461 9273</p>
    </section>
  </main>
</body>
</html>
```